QV - menu design

Hi,

We require elegant menu design for upscale restaurant. Please find attached the logo and the menu items for your reference.

for inspiration, this is a good website: -
http://www.platewhisper.example/bellfoldnotes/about.php

We are very much open for Menu Size suggestions.

unfortunately the place is going under renovation, we don't have updated images to it. the closest look and feel to our place is http://varnelo.example ..

we are also open for creative options on the shape, the styles, etc. as long as it represents the fine dine feel ...

Thanks ...

Dear All,

We wouldlike to extend our apology for not being able to provide feedbacks on everysingle design. We were extremely busy and we have multiple contests opensimultaneously which makes the process even harder.

However,we would like to thank you all for the efforts you have put into designingour menu. It is very much appreciated …

We wishyou all success in your design ventures and we are quite positive that we willbe working with many of you on many projects in the soon future. 

Thanks & Regards,

TLG Team...

 

 

 

Industry/Entity Type

Restaurant

Requirements
Must have
• Please ensure that there are 'some' images in the menu ... this is very important.
Should not have
• IMPORTANT: -

1. Please DO NOT insert any currency sign to the menu
2. Please keep the prices of the menu at the end of the menu items descriptions NOT beside the menu item names. The font of the price should be similar to the menu item description and please DO NOT bold the numbers. the prices should be subtle.

Thank you ...

```html
<!DOCTYPE html>
<html lang="en">
<head>
<meta charset="utf-8">
<title>QV - Menu Cover</title>
<link rel="stylesheet" href="https://fonts.googleapis.com/css2?family=Questrial&family=Playfair+Display:ital@1&display=swap">
<style>
  :root {
    --page: #ffffff;
    --cream: #fbf0cf;
    --cream-light: #fffbf0;
    --cream-edge: #f1dca8;
    --wine: #a51f24;
    --wine-deep: #6e1214;
    --gold: #c8973b;
    --gold-light: #ecd08a;
    --ink: #1d1d1b;
  }
  * { margin: 0; padding: 0; box-sizing: border-box; }
  html, body { width: 1200px; height: 1000px; overflow: hidden; background: var(--page); }
  .canvas { position: relative; width: 1200px; height: 1000px; }

  .menu-cover {
    position: absolute; left: 405px; top: 53px; width: 390px; height: 894px;
    background: radial-gradient(ellipse at 45% 68%, var(--cream-light) 0%, var(--cream) 55%, var(--cream-edge) 100%);
    box-shadow: 3px 4px 8px rgba(0,0,0,0.35);
    overflow: hidden;
  }
  .spine-band {
    position: absolute; left: 0; top: 0; width: 53px; height: 100%;
    background: linear-gradient(180deg, #c9353a 0%, var(--wine) 45%, var(--wine-deep) 100%);
  }
  .spine-rule { position: absolute; top: 0; height: 100%; width: 2px; background: var(--gold); }
  .spine-rule.outer { left: 4px; }
  .spine-rule.inner { left: 46px; }
  .border-pattern {
    position: absolute; left: 53px; top: 0; width: 18px; height: 100%;
    background: linear-gradient(90deg, var(--gold) 0%, var(--gold-light) 50%, var(--gold) 100%);
  }

  .badge-ornament {
    position: absolute; left: 146px; top: 78px; width: 150px; height: 150px;
    background: radial-gradient(circle, rgba(200,151,59,0.35) 0%, rgba(200,151,59,0.12) 55%, rgba(200,151,59,0) 72%);
  }
  .gold-rule { position: absolute; height: 1px; background: linear-gradient(90deg, rgba(200,151,59,0), var(--gold), rgba(200,151,59,0)); }

  .menu-badge {
    position: absolute; left: 166px; top: 98px; width: 110px; height: 110px; border-radius: 50%;
    background: radial-gradient(circle at 40% 30%, #3a3a3a 0%, #050505 70%);
    border: 4px solid var(--gold);
    box-shadow: 0 0 0 2px var(--gold-light);
    display: flex; align-items: center; justify-content: center;
  }
  .menu-badge-label {
    font-family: "Playfair Display", serif; font-style: italic; font-size: 19px; color: #ffffff;
  }

  .venue-name {
    position: absolute; left: 90px; top: 440px; width: 280px; text-align: center;
    font-family: "Questrial", sans-serif; color: var(--ink); font-weight: 400;
  }
  .venue-name .initials { display: block; font-size: 150px; line-height: 1; letter-spacing: 4px; }
  .venue-name .full { display: block; font-size: 24px; letter-spacing: 5px; margin-top: 10px; }

  .cutlery-ornament {
    position: absolute; left: 156px; top: 684px; width: 130px; height: 130px;
    background: radial-gradient(circle, rgba(200,151,59,0.4) 0%, rgba(200,151,59,0.12) 58%, rgba(200,151,59,0) 72%);
  }
  .cutlery-badge { position: absolute; left: 166px; top: 694px; width: 110px; height: 110px; }
</style>
</head>
<body>
<main class="canvas">
  <article class="menu-cover">
    <div class="spine-band"></div>
    <div class="spine-rule outer"></div>
    <div class="spine-rule inner"></div>
    <div class="border-pattern" role="img" aria-label="Gold ornamental chain border"></div>

    <div class="gold-rule" style="left:105px; top:133px; width:232px;"></div>
    <div class="gold-rule" style="left:105px; top:169px; width:232px;"></div>
    <div class="badge-ornament" role="img" aria-label="Gold flourish ornament around the menu badge"></div>
    <div class="menu-badge"><span class="menu-badge-label">Menu</span></div>

    <h1 class="venue-name">
      <span class="initials">QV</span>
      <span class="full">QUILL VALE CAFÉ</span>
    </h1>

    <div class="gold-rule" style="left:105px; top:723px; width:232px;"></div>
    <div class="gold-rule" style="left:105px; top:773px; width:232px;"></div>
    <div class="cutlery-ornament" role="img" aria-label="Gold flourish ornament behind the cutlery badge"></div>
    <svg class="cutlery-badge" viewBox="0 0 110 110" aria-hidden="true">
      <rect x="24" y="24" width="62" height="62" transform="rotate(45 55 55)" fill="#0d0d0d" stroke="var(--gold)" stroke-width="3"/>
      <g fill="var(--gold)">
        <ellipse cx="42" cy="44" rx="4" ry="8"/>
        <rect x="41" y="50" width="2" height="24" rx="1"/>
        <rect x="52" y="36" width="6" height="20" rx="3"/>
        <rect x="54" y="54" width="2" height="22" rx="1"/>
        <rect x="64" y="36" width="1.4" height="12"/>
        <rect x="66.3" y="36" width="1.4" height="12"/>
        <rect x="68.6" y="36" width="1.4" height="12"/>
        <rect x="64" y="46" width="6" height="4" rx="2"/>
        <rect x="66" y="49" width="2" height="25" rx="1"/>
      </g>
    </svg>
  </article>
</main>
</body>
</html>
```